Ich biete Employer-Branding-Beratung für mittelständische Unternehmen, d.h. ich entwickle für und mit meinen Kunden ihre Arbeitgebermarke und Arbeitgeberkommunikation, um leichter neue Mitarbeitende zu finden.
Meine Zielgruppe: mittelständische Unternehmen (1.000-4.000 Mitarbeitende), dort v.a. die Personalabteilung, meist Frauen
- Klappkarte im Format DIN lang. Die Karte soll sich dafür eignen, sie auf den Schreibtisch zu stellen.
- Corporate Design siehe Anhang. Darin ist bereits ein Entwurf für eine Karte enthalten. Der darf gern genau so übernommen werden. Ich freue mich aber auch über gute neue Entwürfe, die das CD aufgreifen.
- Seite 1: Logo & Zitat & Autor: 'Wege entstehen dadurch, dass man sie geht.' // Otto Rembel
- Seite 2: Text: Auf ein Jahr 2024 mit neuen Wegen!
- Seite 3: leer
- Seite 4: Adresse/Kontaktdaten:
Friederike Storm
Die Teamkultur-Expertin
Lindenweg 42
10115 Berlin
T +49 (15 23) 917 20 48
E fs@die-teamkultur-expertin.de
Hinweis: Die Karte wird in durchsichtigen Umschlägen verschickt, die Adresse sollte so kontrastreich sein, dass man sie auch durch den Umschläge sehen kann, falls Briefe zurück kommen.

```html
<!DOCTYPE html>
<html lang="de">
<head>
<meta charset="utf-8">
<title>Klappkarte DIN lang – Die Teamkultur-Expertin</title>
<link rel="stylesheet" href="https://fonts.googleapis.com/css2?family=Montserrat:wght@200;300;400;600&display=swap">
<style>
  :root {
    --bg: #c3c4ca;
    --navy: #163d5e;
    --maroon-dark: #470c28;
    --maroon: #531334;
    --ink-light: #ffffff;
    --quote-ink: #f4e7ef;
    --author-ink: #c79cb4;
    --paper: #ffffff;
    --photo-sky: #a9d6d3;
    --photo-mid: #6d7e99;
    --photo-deep: #2c2f45;
  }
  * { margin: 0; padding: 0; box-sizing: border-box; }
  html, body { width: 860px; height: 1200px; overflow: hidden; }
  body {
    background: var(--bg);
    font-family: "Montserrat", Arial, sans-serif;
    position: relative;
  }
  .brand-mark {
    position: absolute;
    top: 130px;
    right: 64px;
    display: flex;
    align-items: center;
    gap: 14px;
  }
  .brand-mark .dot {
    width: 22px; height: 22px; border-radius: 50%;
    background: var(--navy);
  }
  .brand-mark .name {
    font-size: 26px;
    font-weight: 300;
    letter-spacing: 0.04em;
    color: var(--navy);
    text-transform: uppercase;
  }
  .card-spread {
    position: absolute;
    left: 64px;
    width: 732px;
    height: 175px;
    box-shadow: 0 6px 14px rgba(0,0,0,0.28);
    overflow: hidden;
  }
  .card-spread svg.panels {
    position: absolute; inset: 0;
    width: 732px; height: 175px;
  }
  .card-inside { top: 420px; }
  .card-outside { top: 680px; background: var(--paper); }

  .photo-brand {
    position: absolute;
    font-size: 8px;
    font-weight: 300;
    letter-spacing: 0.05em;
    text-transform: uppercase;
    color: var(--ink-light);
  }
  .photo-brand.left { left: 14px; bottom: 16px; }
  .photo-brand.right { right: 12px; bottom: 16px; }

  .contact {
    position: absolute;
    left: 193px;
    top: 48px;
    color: var(--ink-light);
    font-size: 7.4px;
    font-weight: 300;
    line-height: 1.32;
  }
  .contact .person { font-weight: 600; text-transform: uppercase; }
  .contact .role { text-transform: uppercase; margin-bottom: 9px; }
  .contact .address { margin-bottom: 8px; }

  .quote {
    position: absolute;
    left: 387px;
    top: 28px;
    color: var(--quote-ink);
    font-weight: 300;
    text-transform: uppercase;
    line-height: 1;
  }
  .quote .line { display: block; font-size: 18px; margin-bottom: 4px; letter-spacing: 0.02em; }
  .quote .line.lead { font-size: 26px; margin-bottom: 5px; }
  .quote .line.last { font-size: 24px; }
  .quote .small { font-size: 16px; }
  .quote .author {
    display: block;
    margin-top: 6px;
    font-size: 7.6px;
    color: var(--author-ink);
    letter-spacing: 0.03em;
  }

  .greeting {
    position: absolute;
    left: 36px;
    top: 58px;
    color: var(--ink-light);
    font-weight: 200;
    text-transform: uppercase;
    line-height: 1.25;
    font-size: 27px;
    letter-spacing: 0.01em;
  }
  .greeting .small { font-size: 19px; }
</style>
</head>
<body>

  <div class="brand-mark">
    <span class="dot"></span>
    <span class="name">Die Teamkultur-Expertin</span>
  </div>

  <section class="card-spread card-inside" aria-label="Innenseite: Kontakt und Zitat">
    <svg class="panels" viewBox="0 0 732 175" aria-hidden="false">
      <defs>
        <linearGradient id="mountainLeft" x1="0" y1="0" x2="0" y2="1">
          <stop offset="0" stop-color="#b3e0dc"/>
          <stop offset="0.45" stop-color="#7d8fa6"/>
          <stop offset="1" stop-color="#2a2c40"/>
        </linearGradient>
        <linearGradient id="mountainRight" x1="0" y1="0" x2="0" y2="1">
          <stop offset="0" stop-color="#c2ecea"/>
          <stop offset="0.5" stop-color="#7f93a8"/>
          <stop offset="1" stop-color="#3a3c52"/>
        </linearGradient>
      </defs>
      <rect x="0" y="0" width="732" height="175" fill="var(--maroon)"/>
      <polygon points="160,0 367,0 367,175 140,175" fill="var(--maroon-dark)"/>
      <polygon points="0,0 177,0 141,175 0,175" fill="url(#mountainLeft)" role="img" aria-label="Foto: Bergketten im Dunst"/>
      <polygon points="592,0 732,0 732,175 557,175" fill="url(#mountainRight)" role="img" aria-label="Foto: Steintreppe über Bergen zu einer offenen Tür"/>
    </svg>

    <span class="photo-brand left">Die Teamkultur-Expertin</span>
    <span class="photo-brand right">Die Teamkultur-Expertin</span>

    <div class="contact">
      <div class="person">Friederike Storm</div>
      <div class="role">Die Teamkultur-Expertin</div>
      <div class="address">Lindenweg 42<br>10115 Berlin</div>
      <div>T +49 (15 23) 917 20 48<br>E fs@die-teamkultur-expertin.de</div>
    </div>

    <p class="quote">
      <span class="line lead">Wege</span>
      <span class="line">Entstehen</span>
      <span class="line">dadurch, dass</span>
      <span class="line last">Man <span class="small">sie</span> geht.</span>
      <span class="author">Otto Rembel</span>
    </p>
  </section>

  <section class="card-spread card-outside" aria-label="Außenseite: Neujahrsgruß">
    <svg class="panels" viewBox="0 0 732 175">
      <polygon points="0,0 358,0 341,175 0,175" fill="var(--navy)"/>
    </svg>
    <p class="greeting">
      <span class="small">Auf ein</span> Jahr 2024<br>
      <span class="small">mit</span> neuen Wegen!
    </p>
  </section>

</body>
</html>
```